Playful Website Design Needed Pet Sitting and Dog Walking Business

Need a simple one page Web Design Built on WordPress.
Sections:

About Us
Services Provided
Costs
Contact Us
Intake Form (Questionnaire that goes to email)
See us in Action

Industry/Entity Type

Pet Sitting and Dog Walking

Number of Pages Required

1 page

Font styles to use
Other font styles liked:
• See the Business Card Font and use that.

Colors
EE7325
F08F49
F5BC92
FAE3D3
FDF4ED

Requirements
Must have
• See attached Logo Design, with Font's and Colors Use these as theme guide

```html
<!DOCTYPE html>
<html lang="en">
<head>
<meta charset="utf-8">
<title>Paw Haven Sitters</title>
<link href="https://fonts.googleapis.com/css2?family=Libre+Baskerville:ital,wght@0,400;0,700;1,400&family=Open+Sans:wght@400;600;700&display=swap" rel="stylesheet">
<style>
:root{
  --orange:#e8490f;
  --orange-soft:#ee7325;
  --yellow:#e8a82e;
  --purple:#6a0dc4;
  --ink:#1e1e1e;
  --text:#555;
  --grey:#f2f2f2;
  --line:#e2e2e2;
  --white:#fff;
}
*{box-sizing:border-box;margin:0;padding:0}
html,body{width:1200px;height:4170px;overflow:hidden;background:var(--white)}
body{position:relative;font-family:"Open Sans",sans-serif;color:var(--text)}
.abs{position:absolute}
.serif{font-family:"Libre Baskerville",serif}

/* top bar */
.topbar{left:0;top:0;width:1200px;height:72px}
.topbar .info{position:absolute;top:17px;font-size:12px;color:var(--white);display:flex;align-items:center;gap:8px}
.social{display:flex;gap:14px}
.social span{width:11px;height:11px;border-radius:50%;background:currentColor;display:block}
.topbar .social{position:absolute;right:80px;top:22px;color:var(--white)}

/* header */
.brand{font-family:"Libre Baskerville",serif;font-weight:700;color:var(--orange);font-size:20px;display:flex;align-items:center;gap:10px}
.brand i{width:18px;height:18px;border-radius:50%;background:var(--yellow);display:block}
.nav{right:103px;top:111px;display:flex;gap:44px;font-size:14px;font-weight:600;color:var(--ink);letter-spacing:.5px}

/* hero */
.hero{left:0;top:170px;width:1200px;height:672px;background:linear-gradient(100deg,#ece9e6 0%,#dcd6d0 45%,#b9b0a8 75%,#8f8780 100%)}
.hero h1{position:absolute;left:122px;top:160px;font-family:"Libre Baskerville",serif;font-weight:700;font-size:50px;line-height:65px;color:var(--ink);letter-spacing:1px}
.hero h1 em{font-style:normal;color:var(--orange)}
.btn{display:flex;align-items:center;justify-content:center;border-radius:30px;color:var(--white);font-weight:700}
.hero .btn{position:absolute;left:108px;top:386px;width:182px;height:54px;background:var(--orange);font-size:22px;letter-spacing:.5px}
.arrow{position:absolute;top:310px;width:52px;height:52px;border-radius:50%;background:rgba(160,160,160,.55);color:#eee;display:flex;align-items:center;justify-content:center;font-size:18px}

/* section headings */
.kicker{width:1200px;left:0;text-align:center;font-family:"Libre Baskerville",serif;font-style:italic;font-size:12px;color:#666}
.title{width:1200px;left:0;text-align:center;font-family:"Libre Baskerville",serif;font-weight:700;color:var(--ink);font-size:37px;letter-spacing:1px}
.pawline{left:0;width:1200px;display:flex;justify-content:center;align-items:center;gap:8px;color:#999;font-size:10px;letter-spacing:2px}

/* welcome */
.welcome-photo{left:81px;top:1069px;width:508px;height:382px;background:linear-gradient(160deg,#f2efec,#ddd6cf 55%,#c7a47c 80%,#e6e0da)}
.welcome-text{left:620px;top:1070px;width:500px;font-size:12.5px;line-height:25px;color:var(--text)}
.welcome-text p{margin-bottom:17px}
.ticks{list-style:none;margin-top:20px}
.ticks li{display:flex;align-items:center;gap:12px;font-weight:600;color:#333;margin-bottom:4px}
.ticks li::before{content:"";width:8px;height:8px;border:2px solid #f0a48a;border-radius:50%}
.welcome .btn{left:620px;top:1400px;width:196px;height:49px;background:var(--yellow);font-size:11.5px;letter-spacing:.5px}

/* feature band */
.band{left:0;top:1579px;width:1200px;height:265px;background:var(--grey)}
.feature{top:1632px;width:332px;height:129px;background:var(--white);box-shadow:0 2px 6px rgba(0,0,0,.08);display:flex;align-items:center;gap:22px;padding-left:28px}
.feature h4{font-family:"Libre Baskerville",serif;font-weight:400;font-size:14px;color:#333;margin-bottom:9px}
.feature p{font-size:12px;color:#444;font-weight:600}

/* services */
.services-photo{left:518px;top:2050px;width:682px;height:553px;background:radial-gradient(ellipse at 60% 50%,#f3eee5 0%,#efe6d8 40%,#f6f2ec 70%,#fff 100%)}
.service{width:508px;height:180px;background:var(--white);border:1px solid var(--line);padding:34px 40px 0 106px;box-shadow:0 1px 4px rgba(0,0,0,.05)}
.service svg{position:absolute;left:30px;top:38px}
.service h4{font-family:"Libre Baskerville",serif;font-size:15px;color:#222;margin-bottom:14px}
.service p{font-size:12px;line-height:24px;color:#555}
.dots{left:0;width:1200px;top:2525px;display:flex;justify-content:center;gap:10px}
.dots span{width:8px;height:8px;border-radius:50%;border:1px solid #bbb}
.dots span.on{background:var(--yellow);border-color:var(--yellow)}
.floating-paw{left:1152px;top:2532px;width:36px;height:60px;border-radius:18px;background:var(--orange);display:flex;align-items:center;justify-content:center}

/* costs */
.cost-text{left:230px;width:740px;top:2742px;text-align:center;font-size:14px;line-height:26px;color:#555}
.price{top:2845px;width:240px;text-align:center;font-family:"Libre Baskerville",serif;font-weight:700;font-size:40px;color:var(--ink)}
.cost .btn{top:2922px;height:49px;font-size:21px}
.divider{top:2845px;width:1px;height:125px;background:var(--line)}

/* appointment */
.appointment{left:0;top:3149px;width:1200px;height:715px;background:var(--orange)}
.appointment .kicker,.appointment .title{color:var(--white)}
.field{height:43px;border-radius:22px;background:var(--white);font-size:12px;color:#888;padding:0 22px;display:flex;align-items:center;justify-content:space-between}
.field.area{align-items:flex-start;padding-top:14px;border-radius:18px}
.appointment .btn{left:512px;top:3667px;width:176px;height:48px;background:var(--yellow);font-size:12px}

/* footer */
.footer-brand{left:0;width:1200px;top:3935px;justify-content:center}
.footer .social{left:0;width:1200px;top:4042px;justify-content:center;color:#777;position:absolute}
.copy{left:0;width:1200px;top:4100px;text-align:center;font-size:12.5px;color:#444}
</style>
</head>
<body>

<!-- top bar -->
<svg class="abs" style="left:0;top:0" width="1200" height="72" viewBox="0 0 1200 72" aria-hidden="true">
  <path d="M0 0H1200V60l-20 3-25-4-30 5-22-3-30 4-28-5-24 4-30-3-26 5-30-4-22 3-30-4-26 5-28-3-24 3-30-4-28 5-22-4-30 3-26-3-28 5-24-4-30 3-28-4-22 5-30-3-26 3-28-4-24 4-30-3-28 5-22-4-30 3-26-4-28 5-24-3-30 3-26-5-22 4-30-3-28 5-24-4-30 3-22-3-28 5-26-4-30 3-24-4-28 4-22 3-30-4-26 3L0 62Z" fill="var(--orange)"/>
</svg>
<div class="abs topbar">
  <div class="info" style="left:81px">
    <svg width="10" height="13" viewBox="0 0 10 13"><path d="M5 0a5 5 0 0 1 5 5c0 3.5-5 8-5 8S0 8.5 0 5a5 5 0 0 1 5-5zm0 3a2 2 0 1 0 0 4 2 2 0 0 0 0-4z" fill="#fff"/></svg>
    18 Maple Row, Cedar St. FL
  </div>
  <div class="info" style="left:298px">
    <svg width="12" height="12" viewBox="0 0 12 12"><path d="M2.5 0l2 3-1.3 1.4a7 7 0 0 0 4.4 4.4L9 7.5l3 2-1.3 2.3C5 12 0 7 .2 1.3Z" fill="#fff"/></svg>
    +(1) 555 010 4477
  </div>
  <div class="info" style="left:465px">
    <svg width="13" height="10" viewBox="0 0 13 10"><rect width="13" height="10" rx="1" fill="#fff"/><path d="M1 1l5.5 4.5L12 1" stroke="#e8490f" fill="none" stroke-width="1.2"/></svg>
    hello@pawhavensitters.com
  </div>
  <div class="social"><span></span><span></span><span></span><span></span><span></span></div>
</div>

<!-- header -->
<div class="abs brand" style="left:78px;top:108px"><i></i>Paw Haven Sitters</div>
<nav class="abs nav"><span>ABOUT</span><span>SERVICES</span><span>COSTS</span><span>CONTACT US</span></nav>

<!-- hero -->
<section class="abs hero" role="img" aria-label="Photo of a fluffy white and grey cat held in a person's arm">
  <h1>We Feed, Walk and<br>Play with your <em>LovingPet,</em><br>each visit!</h1>
  <div class="btn">CALL NOW!</div>
  <div class="arrow" style="left:41px">&#8249;</div>
  <div class="arrow" style="right:41px">&#8250;</div>
</section>
<svg class="abs" style="left:0;top:826px" width="1200" height="20" viewBox="0 0 1200 20" aria-hidden="true">
  <path d="M0 16l30-4 28 3 26-5 30 4 22-3 30 4 28-5 24 3 30-3 26 4 28-4 22 3 30-4 26 5 28-3 24 2 30-4 28 4 22-3 30 3 26-5 28 4 24-3 30 4 28-4 22 3 30-3 26 4 28-5 24 3 30-2 26 3 28-4 22 3 30-3 24 4 28-4 26 3 30-3 22 4 28-5 30 3 24-2 26 4 30-3 28 3 V20H0Z" fill="#fff"/>
</svg>

<!-- welcome -->
<section class="welcome">
  <div class="abs pawline" style="top:924px">::::::
    <svg width="24" height="20" viewBox="0 0 24 20"><g fill="var(--orange)"><ellipse cx="12" cy="14" rx="6" ry="5"/><circle cx="4" cy="8" r="2.6"/><circle cx="9" cy="3.5" r="2.6"/><circle cx="15" cy="3.5" r="2.6"/><circle cx="20" cy="8" r="2.6"/></g></svg>
  ::::::</div>
  <p class="abs kicker" style="top:964px">Because We Really Care About Your Pets</p>
  <h2 class="abs title" style="top:990px">Welcome to Paw Haven Sitters</h2>
  <div class="abs welcome-photo" role="img" aria-label="Photo of a tabby kitten sleeping on a blanket with a green ball and a red cushion"></div>
  <div class="abs welcome-text">
    <p>Broadcast neglectful and poignantly well until and some listlessly amidst suc cessful concentrically ably dachshund more far but forwardly echidna outside tiger split thanks far vibrantly gosh hence pangolin however notwithstanding leapt untruthful gauchely yikes komodo dully more.</p>
    <p>As abandoned winced this more far wow jeepers near more wow goodness so revealed much along worm some grasshopper.</p>
    <ul class="ticks">
      <li>Abore et dolore magna aliqua ut enim veniam</li>
      <li>Quis nostrud exercitation ullamco laboris nisi aliquip</li>
      <li>Eiusmod tempor incididunt labore.</li>
    </ul>
  </div>
  <div class="abs btn">VIEW OUR SERVICES</div>
</section>

<!-- feature band -->
<div class="abs band"></div>
<svg class="abs" style="left:0;top:1824px" width="1200" height="22" viewBox="0 0 1200 22" aria-hidden="true">
  <path d="M0 14l30-3 26 4 28-5 30 3 24-2 28 4 30-4 22 3 28-3 30 5 26-4 28 2 24-3 30 4 28-4 22 3 30-2 26 3 28-5 24 4 30-3 28 3 22-4 30 3 26-2 28 4 24-4 30 3 28-3 22 4 30-4 26 3 28-2 24 3 30-4 26 4 28-3 22 2 30-4 24 4 28-3 26 3 30-4 22 3 28-3 30 4 24-2 26 3 30-4 28 3V22H0Z" fill="#fff"/>
</svg>
<div class="abs feature" style="left:81px">
  <svg width="44" height="40" viewBox="0 0 44 40"><path d="M6 4h32c4 0 6 4 4 8l-6 6v12c0 5-4 8-8 8H16c-4 0-8-3-8-8V18l-6-6C0 8 2 4 6 4z" fill="var(--orange)"/><circle cx="16" cy="18" r="2.5" fill="#fff"/><circle cx="28" cy="18" r="2.5" fill="#fff"/><ellipse cx="22" cy="27" rx="4" ry="3" fill="#fff"/></svg>
  <div><h4>We Heal Pets</h4><p>Quick Veterinary Services</p></div>
</div>
<div class="abs feature" style="left:434px">
  <svg width="44" height="40" viewBox="0 0 44 40"><g fill="var(--yellow)"><circle cx="35" cy="5" r="5"/><circle cx="39" cy="11" r="5"/><circle cx="5" cy="29" r="5"/><circle cx="9" cy="35" r="5"/><path d="M32 7l5 5L12 35l-5-5Z"/></g></svg>
  <div><h4>We Care Pets</h4><p>Pet Sheltering &amp; Adoption</p></div>
</div>
<div class="abs feature" style="left:788px">
  <svg width="44" height="40" viewBox="0 0 44 40"><g fill="var(--purple)"><ellipse cx="22" cy="28" rx="11" ry="9"/><circle cx="6" cy="16" r="5"/><circle cx="15" cy="6" r="5"/><circle cx="29" cy="6" r="5"/><circle cx="38" cy="16" r="5"/></g></svg>
  <div><h4>We Love Pets</h4><p>Show Love &amp; Donate Us</p></div>
</div>

<!-- services -->
<section class="services">
  <div class="abs services-photo" role="img" aria-label="Photo of colourful pet toys, rope bones, a food bowl and a collar laid out on white"></div>
  <div class="abs pawline" style="top:1930px">::::::
    <svg width="24" height="20" viewBox="0 0 24 20"><g fill="var(--orange)"><ellipse cx="12" cy="14" rx="6" ry="5"/><circle cx="4" cy="8" r="2.6"/><circle cx="9" cy="3.5" r="2.6"/><circle cx="15" cy="3.5" r="2.6"/><circle cx="20" cy="8" r="2.6"/></g></svg>
  ::::::</div>
  <p class="abs kicker" style="top:1971px">Because We Really Care About Your Pets</p>
  <h2 class="abs title" style="top:2000px">Our Services</h2>

  <div class="abs service" style="left:81px;top:2077px">
    <svg width="56" height="56" viewBox="0 0 56 56" fill="none" stroke="#222" stroke-width="1.8"><circle cx="8" cy="8" r="5"/><circle cx="20" cy="6" r="5"/><path d="M11 12l18 30M17 10L6 44"/><rect x="30" y="18" width="22" height="8"/><path d="M32 26v9M36 26v9M40 26v9M44 26v9M48 26v9M38 18v-6h6v6"/></svg>
    <h4>Pet Grooming</h4>
    <p>Abore et dolore magna aliqua ut enim minim veniam quis nostrud exercitation ullamco laboris nisi aliquip eiusmod tempor incididunt labore.</p>
  </div>
  <div class="abs service" style="left:612px;top:2077px">
    <svg width="56" height="56" viewBox="0 0 56 56" fill="none" stroke="#222" stroke-width="1.8"><circle cx="28" cy="20" r="12"/><path d="M17 15c-6-4-12 2-8 10M39 15c6-4 12 2 8 10"/><ellipse cx="28" cy="25" rx="3" ry="2"/><path d="M18 32v18h20V32M24 50v-8M32 50v-8"/></svg>
    <h4>Pet Sitting</h4>
    <p>Abore et dolore magna aliqua ut enim minim veniam quis nostrud exercitation ullamco laboris nisi aliquip eiusmod tempor incididunt labore.</p>
  </div>
  <div class="abs service" style="left:81px;top:2284px">
    <svg width="56" height="56" viewBox="0 0 56 56" fill="none" stroke="#222" stroke-width="1.8"><circle cx="28" cy="20" r="12"/><path d="M17 15c-6-4-12 2-8 10M39 15c6-4 12 2 8 10"/><ellipse cx="28" cy="25" rx="3" ry="2"/><path d="M18 32v18h20V32M24 50v-8M32 50v-8"/></svg>
    <h4>Pet Training</h4>
    <p>Abore et dolore magna aliqua ut enim minim veniam quis nostrud exercitation ullamco laboris nisi aliquip eiusmod tempor incididunt labore.</p>
  </div>
  <div class="abs service" style="left:612px;top:2284px">
    <svg width="56" height="56" viewBox="0 0 56 56" fill="none" stroke="#222" stroke-width="1.8"><rect x="3" y="14" width="50" height="30" rx="2"/><path d="M20 14V8h16v6M10 14v30M46 14v30"/><circle cx="28" cy="29" r="9"/><path d="M28 24v10M23 29h10"/></svg>
    <h4>Pet Vaccination</h4>
    <p>Abore et dolore magna aliqua ut enim minim veniam quis nostrud exercitation ullamco laboris nisi aliquip eiusmod tempor incididunt labore.</p>
  </div>
  <div class="abs dots"><span class="on"></span><span></span><span></span></div>
  <div class="abs floating-paw"><svg width="22" height="20" viewBox="0 0 24 20"><g fill="#fff"><ellipse cx="12" cy="14" rx="6" ry="5"/><circle cx="4" cy="8" r="2.6"/><circle cx="9" cy="3.5" r="2.6"/><circle cx="15" cy="3.5" r="2.6"/><circle cx="20" cy="8" r="2.6"/></g></svg></div>
</section>

<!-- costs -->
<section class="cost">
  <h2 class="abs title" style="top:2675px">Our Service Cost</h2>
  <p class="abs cost-text">More forwardly echidna outside tiger split thanks vibrantly gosh hence pangolin however notwithstanding leapt untruthful gauchely yikes komodo successful concentrically dully more.</p>
  <div class="abs price" style="left:213px">$8</div>
  <div class="abs divider" style="left:461px"></div>
  <div class="abs price" style="left:469px">$8</div>
  <div class="abs divider" style="left:717px"></div>
  <div class="abs price" style="left:733px">$8</div>
  <div class="abs btn" style="left:244px;width:178px;background:var(--orange)">Per Visit</div>
  <div class="abs btn" style="left:504px;width:172px;background:var(--yellow)">Per Visit</div>
  <div class="abs btn" style="left:764px;width:166px;background:var(--purple)">Per Visit</div>
</section>

<!-- appointment -->
<section class="abs appointment"></section>
<svg class="abs" style="left:0;top:3855px" width="1200" height="20" viewBox="0 0 1200 20" aria-hidden="true">
  <path d="M0 0H1200V8l-28 4-26-3-30 5-24-4-28 3-30-4-22 5-30-3-26 4-28-5-24 3-30-2-28 4-22-4-30 3-26-3-28 5-24-4-30 3-28-3-22 4-30-5-26 4-28-2-24 3-30-4-28 4-22-3-30 3-26-4-28 5-24-3-30 2-26-3-28 4-22-3-30 4-24-4-28 3-26-2-30 4-22-5-28 3-30-3-24 4-26-3-30 3-28-4V0Z" fill="var(--orange)"/>
</svg>
<div class="abs pawline" style="top:3230px;color:#fff">::::::
  <svg width="24" height="20" viewBox="0 0 24 20"><g fill="#fff"><ellipse cx="12" cy="14" rx="6" ry="5"/><circle cx="4" cy="8" r="2.6"/><circle cx="9" cy="3.5" r="2.6"/><circle cx="15" cy="3.5" r="2.6"/><circle cx="20" cy="8" r="2.6"/></g></svg>
::::::</div>
<p class="abs kicker" style="top:3271px;color:#fff">Because We Really Care About Your Pets</p>
<h2 class="abs title" style="top:3294px;color:#fff;font-size:33px;letter-spacing:0">Get An Appointment</h2>
<div class="abs field" style="left:81px;top:3375px;width:332px">Name</div>
<div class="abs field" style="left:434px;top:3375px;width:332px">Email</div>
<div class="abs field" style="left:788px;top:3375px;width:332px">Phone #</div>
<div class="abs field" style="left:81px;top:3442px;width:332px">Date &amp; Time
  <svg width="12" height="12" viewBox="0 0 12 12"><rect x="1" y="2" width="10" height="9" fill="none" stroke="#777"/><path d="M1 5h10M4 1v2M8 1v2" stroke="#777"/></svg></div>
<div class="abs field" style="left:434px;top:3442px;width:332px">Pet Category</div>
<div class="abs field" style="left:788px;top:3442px;width:332px">Service Type</div>
<div class="abs field area" style="left:81px;top:3508px;width:1039px;height:125px">Your Comments...</div>
<div class="abs btn" style="left:512px;top:3667px;width:176px;height:48px;background:var(--yellow);font-size:12px">SEND REQUEST</div>

<!-- footer -->
<footer class="footer">
  <div class="abs brand footer-brand" style="display:flex;font-size:24px"><i style="width:22px;height:22px"></i>Paw Haven Sitters</div>
  <div class="social"><span></span><span></span><span></span><span></span><span></span></div>
  <p class="abs copy">Copyright 2022 pawhavensitters.com All rights reserved.</p>
</footer>

</body>
</html>
```